Wordpress Home Page

Management Consulting firm is seeking a creative wordpress designer to develop a home page our B to B website http://www.quorvanta.com. The owner is really looking for a home page that can tie in all the key subsections using recent post lists and sliders.

We run on wordpress with a wootheme. You can see our dev site to get a feel of the new colors we are using. http://dev.quorvanta.com

Industry/Entity Type

Management Consulting

Requirements
Must have
• Here are some features we are looking for:
* thematic sliders that represent our top sections for the site. Each slide would have 3 sections for the sub sections of the top section. We have a mockup

* A creative way to display most recent posts from the different subsections.

* Nice separation using graphics.

```html
<!DOCTYPE html>
<html lang="en">
<head>
<meta charset="utf-8">
<title>Quorvanta – Home</title>
<link rel="stylesheet" href="https://fonts.googleapis.com/css2?family=Arimo:wght@400;700&display=swap">
<style>
:root{
  --page:#ececec;
  --topbar-a:#0f5479;
  --topbar-b:#0a3e5c;
  --white:#ffffff;
  --text:#4a4a4a;
  --dark:#333333;
  --muted:#8a8a8a;
  --orange-a:#f6923a;
  --orange-b:#e8701b;
  --orange-text:#e0650a;
  --phone:#f07a1a;
  --green:#7cb518;
  --blue-title:#1d6b9e;
  --slider-frame:#b9d8ec;
  --panel:#f2f2f2;
  --line:#dedede;
}
*{box-sizing:border-box;margin:0;padding:0}
html,body{width:932px;height:1200px;overflow:hidden}
body{background:linear-gradient(#dcdcdc 0,var(--page) 140px,var(--page));font-family:"Arimo",sans-serif;color:var(--text);position:relative}
.abs{position:absolute}
.topbar{left:0;top:0;width:932px;height:39px;background:linear-gradient(var(--topbar-a),var(--topbar-b));border-bottom:1px solid #5b8fb0}
.account-links{right:70px;top:0;height:39px;display:flex;align-items:center;gap:10px;color:#fff;font-size:10.5px}
.account-links span.sep{opacity:.8}
.account-links .link{display:flex;align-items:center;gap:5px}
.sheet{left:70px;top:58px;width:792px;height:1063px;background:var(--white)}
.brand{left:86px;top:73px;display:flex;align-items:center;gap:10px}
.brand-mark{width:54px;height:54px;border-radius:50%;background:radial-gradient(circle at 40% 35%,#f4f4f4,#9aa6ae);border:2px solid #8a969e}
.brand-name{font-size:23px;letter-spacing:4px;color:var(--dark);line-height:1}
.brand-tag{font-size:8.5px;color:#555;margin-top:3px}
.callus{right:84px;top:77px;font-size:14.5px;color:#9a9a9a}
.callus b{color:var(--phone);font-weight:700}
.search{left:683px;top:106px;width:164px;height:28px;border:1px solid #d4d4d4;font-size:8.5px;color:#444;padding:9px 0 0 11px}
.search svg{position:absolute;right:9px;top:7px}
.nav{left:77px;top:155px;width:779px;height:38px;background:linear-gradient(var(--orange-a),var(--orange-b));border:1px solid #d86310;border-radius:2px;display:flex}
.nav a{color:#fff;font-weight:700;font-size:11px;text-decoration:none;display:flex;align-items:center;justify-content:center;border-right:1px solid #d86310;text-shadow:0 1px 0 rgba(0,0,0,.15)}
.nav a:last-child{border-right:0}
.slider{left:77px;top:198px;width:779px;height:257px;border:5px solid var(--slider-frame);background:#f3f3f5}
.slide-photo{position:absolute;left:323px;top:0;right:0;bottom:0;background:linear-gradient(100deg,#f3f3f5 0,#d9dfe6 25%,#9fb0c0 65%,#5e6e80 100%)}
.slide-title{left:113px;top:261px;font-size:16.5px;color:var(--blue-title)}
.slide-text{left:113px;top:287px;width:264px;font-size:10.5px;line-height:18px;color:#555}
.dots{left:102px;top:418px;display:flex;gap:7px}
.dots i{width:13px;height:13px;border-radius:50%;border:1px solid #9a9a9a;background:radial-gradient(#fff,#dcdcdc)}
.dots i:first-child{background:radial-gradient(#bbb,#999)}
h2{font-weight:400;font-size:15.5px;color:var(--green)}
h2 span{color:var(--dark)}
.welcome{left:79px;top:478px}
.intro{left:79px;top:508px;width:566px;font-size:10.3px;line-height:18px;text-align:justify}
.intro p{margin-bottom:6px}
.rule{height:1px;background:var(--line)}
.features{left:78px;top:649px;display:flex;gap:16px}
.feature{width:178px;height:121px;background:var(--panel);padding:10px 10px 0}
.feature-head{display:flex;gap:14px;height:52px}
.feature-head svg{flex:none}
.feature h3{font-weight:400;font-size:14px;line-height:17.5px;color:var(--orange-text);margin-top:3px}
.feature p{font-size:10.2px;line-height:16.5px;color:#666;text-align:justify;margin-top:6px}
.resources-title{left:664px;top:478px}
.resources{left:663px;top:512px;width:192px}
.resource{height:36px;margin-bottom:8px;background:linear-gradient(#fafafa,#ececec);border:1px solid #e2e2e2;display:flex;align-items:center;gap:13px;padding-left:10px;font-size:12px;color:#444}
.blog-title{left:80px;top:796px}
.blog-arrows{left:831px;top:798px}
.posts{left:80px;top:825px;display:flex;gap:46px}
.post{width:227px}
.post-photo{height:124px;background:#e4e4e4;padding:5px 6px 6px}
.post-photo div{width:100%;height:100%}
.post h4{font-size:11.3px;line-height:16px;color:var(--dark);margin-top:16px;font-weight:700;white-space:nowrap}
.btn{display:inline-block;margin-top:10px;width:77px;height:27px;border:1px solid #dcdcdc;box-shadow:inset 0 -2px 0 #eee;font-size:8.8px;color:#777;text-align:center;line-height:25px}
.partners{left:78px;top:1074px;width:780px;height:24px;display:flex;align-items:center}
.round-arrow{width:18px;height:18px;border-radius:50%;background:#c9c9c9;flex:none;display:flex;align-items:center;justify-content:center}
.partner-list{flex:1;display:flex;justify-content:space-around;align-items:center;font-size:13px;font-weight:700;color:#555}
.partner-list span{display:flex;align-items:center;gap:5px}
.partner-list i{width:9px;height:9px;background:#bbb;display:inline-block}
.footer-links{left:70px;top:1140px;font-size:10.5px;color:#555;display:flex;gap:9px}
.copyright{left:70px;top:1166px;font-size:10.3px;color:#555;display:flex;gap:12px}
.social{left:792px;top:1148px;display:flex;gap:3px}
.social i{width:21px;height:21px;display:block;border-radius:2px}
</style>
</head>
<body>

<header class="topbar abs">
  <div class="account-links abs">
    <span class="link">
      <svg width="14" height="14" viewBox="0 0 14 14"><circle cx="7" cy="4" r="3.2" fill="#fff"/><path d="M1 14c0-4 2.6-6 6-6s6 2 6 6z" fill="#fff"/></svg>My Account</span>
    <span class="sep">|</span>
    <span class="link">
      <svg width="14" height="14" viewBox="0 0 14 14"><rect x="1" y="3" width="10" height="10" fill="none" stroke="#fff" stroke-width="1.5"/><path d="M3.5 7.5l2.5 2.5 7-8" fill="none" stroke="#fff" stroke-width="2"/></svg>Check Out</span>
    <span class="sep">|</span>
    <span class="link">
      <svg width="13" height="14" viewBox="0 0 13 14"><path d="M3 6V4a3.5 3.5 0 0 1 7 0v2" fill="none" stroke="#fff" stroke-width="1.6"/><rect x="1" y="6" width="11" height="8" rx="1" fill="#fff"/></svg>Logout</span>
  </div>
</header>

<main class="sheet abs"></main>

<div class="brand abs">
  <div class="brand-mark"></div>
  <div>
    <div class="brand-name">Quorvanta</div>
    <div class="brand-tag">Performance Benchmarking</div>
  </div>
</div>
<div class="callus abs">Call Us : <b>555-310-4821</b></div>
<div class="search abs">Search
  <svg width="13" height="13" viewBox="0 0 13 13"><circle cx="5" cy="5" r="3.6" fill="none" stroke="#222" stroke-width="2"/><path d="M7.8 7.8l4 4" stroke="#222" stroke-width="2.6"/></svg>
</div>

<nav class="nav abs">
  <a style="width:72px">HOME</a>
  <a style="width:143px">ABOUT QUORVANTA</a>
  <a style="width:126px">BENCHMARKING</a>
  <a style="width:134px">SHOP QUORVANTA</a>
  <a style="width:126px">NEWS &amp; EVENTS</a>
  <a style="width:65px">BLOG</a>
  <a style="flex:1">CONTACT US</a>
</nav>

<section class="slider abs">
  <div class="slide-photo" role="img" aria-label="Contact center agent wearing a headset at a computer, colleagues working in the background"></div>
</section>
<div class="slide-title abs">Contact Center</div>
<p class="slide-text abs">Donec leo metus, dignissim eu quam ut, ultricies blandit elit. Class aptent taciti sociosqu ad litora torquent per conubia nostra, per inceptos himenaeos.</p>
<div class="dots abs"><i></i><i></i><i></i><i></i></div>

<h2 class="welcome abs">Welcome to <span>Quorvanta</span></h2>
<div class="intro abs">
  <p>Curabitur tellus leo, lacinia quis porta sit amet, facilisis et ante. Duis ac aliquet turpis. Nunc luctus tellus et bibendum molestie. Aliquam mattis eleifend tortor, at rhoncus felis sagittis pharetra.</p>
  <p>Donec bibendum neque id dolor fringilla, in egestas nibh facilisis. Suspendisse fermentum libero pharetra diam facilisis, non elementum ante rutrum. Ut et consectetur orci, eget consequat velit. Nam scelerisque est ut arcu vestibulum laoreet. Nulla placerat, sem id pulvinar pretium, odio leo mattis sapien, sit amet ullamcorper libero risus vitae metus. Proin nunc nunc, commodo eu pretium at, dapibus nec nunc. Suspendisse ullamcorper dui dui, sit amet porttitor.</p>
</div>
<div class="rule abs" style="left:78px;top:630px;width:567px"></div>

<section class="features abs">
  <div class="feature">
    <div class="feature-head">
      <svg width="42" height="40" viewBox="0 0 42 40"><path d="M10 2h22l2 22H8z" fill="#e8eef4" stroke="#9aa" /><path d="M21 6v14M15 15l6 7 6-7" stroke="#1e7fd0" stroke-width="4" fill="none"/><path d="M2 26h38v12H2z" fill="#222"/></svg>
      <h3>Instatnt<br>Downloads</h3>
    </div>
    <p>Etiam a laoreet nisi. Vivamus faucibus est nunc, vel vestibulum massa aliquet eget.</p>
  </div>
  <div class="feature">
    <div class="feature-head">
      <svg width="42" height="40" viewBox="0 0 42 40"><path d="M6 4h26v34H6z" fill="#fff" stroke="#999"/><path d="M8 36l8-14 6 6 10-18v26z" fill="#3a9a2a"/><path d="M8 36l6-8 8 4 10-6v10z" fill="#d9302a"/></svg>
      <h3>Data sales</h3>
    </div>
    <p>Etiam a laoreet nisi. Vivamus faucibus est nunc, vel vestibulum massa aliquet eget.</p>
  </div>
  <div class="feature">
    <div class="feature-head">
      <svg width="42" height="40" viewBox="0 0 42 40"><path d="M10 2h22l2 22H8z" fill="#e8eef4" stroke="#9aa" /><path d="M21 6v14M15 15l6 7 6-7" stroke="#1e7fd0" stroke-width="4" fill="none"/><path d="M2 26h38v12H2z" fill="#222"/></svg>
      <h3>Custom Peer<br>Groups</h3>
    </div>
    <p>Etiam a laoreet nisi. Vivamus faucibus est nunc, vel vestibulum massa aliquet eget.</p>
  </div>
</section>

<h2 class="resources-title abs">Our Resources</h2>
<ul class="resources abs" style="list-style:none">
  <li class="resource"><svg width="20" height="22" viewBox="0 0 20 22"><path d="M3 1h10l5 5v15H3z" fill="#fff" stroke="#bbb"/></svg>White Paper</li>
  <li class="resource"><svg width="20" height="22" viewBox="0 0 20 22"><rect x="2" y="10" width="4" height="10" fill="#e33"/><rect x="7" y="5" width="4" height="15" fill="#3a9a2a"/><rect x="12" y="8" width="4" height="12" fill="#2a7ad0"/></svg>Metric of the month</li>
  <li class="resource"><svg width="20" height="22" viewBox="0 0 20 22"><rect x="1" y="4" width="18" height="15" rx="2" fill="#333"/><circle cx="10" cy="12" r="4" fill="#ccc"/></svg>Industry Training</li>
  <li class="resource"><svg width="22" height="22" viewBox="0 0 22 22"><rect x="1" y="3" width="14" height="10" fill="#2a7ad0"/><rect x="7" y="8" width="14" height="10" fill="#5aa6e6" stroke="#fff"/></svg>Service Desk</li>
  <li class="resource"><svg width="20" height="22" viewBox="0 0 20 22"><rect x="1" y="3" width="18" height="12" fill="#444"/><rect x="3" y="5" width="14" height="8" fill="#9fc4e0"/><rect x="6" y="16" width="8" height="3" fill="#888"/></svg>Desktop Support</li>
  <li class="resource"><svg width="20" height="22" viewBox="0 0 20 22"><path d="M3 13a7 7 0 0 1 14 0" fill="none" stroke="#444" stroke-width="2"/><rect x="1" y="12" width="5" height="8" rx="2" fill="#444"/><rect x="14" y="12" width="5" height="8" rx="2" fill="#444"/></svg>Contact Center</li>
</ul>

<h2 class="blog-title abs">Latest Blog Posts</h2>
<svg class="blog-arrows abs" width="22" height="12" viewBox="0 0 22 12"><path d="M7 1L2 6l5 5M15 1l5 5-5 5" fill="none" stroke="#555" stroke-width="2"/></svg>

<section class="posts abs">
  <article class="post">
    <div class="post-photo"><div role="img" aria-label="Trainer presenting to a room of people at computers" style="background:linear-gradient(120deg,#e9eef2,#9cb3c6 50%,#2c5a8c)"></div></div>
    <h4>3 Psychologically-based Approaches<br>to Reducing Call Center Turnover</h4>
    <span class="btn">VIEW MORE</span>
  </article>
  <article class="post">
    <div class="post-photo"><div role="img" aria-label="Businessman lifting a dumbbell in a bright office" style="background:linear-gradient(120deg,#f4f6f8,#dde2e6 55%,#8a9096)"></div></div>
    <h4>3 Psychologically-based Approaches<br>to Reducing Call Center Turnover</h4>
    <span class="btn">VIEW MORE</span>
  </article>
  <article class="post">
    <div class="post-photo"><div role="img" aria-label="Businessman standing at a window overlooking a city" style="background:linear-gradient(120deg,#5b5f63,#b4b8bc 50%,#3e4144)"></div></div>
    <h4>3 Psychologically-based Approaches<br>to Reducing Call Center Turnover</h4>
    <span class="btn">VIEW MORE</span>
  </article>
</section>

<div class="rule abs" style="left:78px;top:1055px;width:776px"></div>

<div class="partners abs">
  <span class="round-arrow"><svg width="8" height="8" viewBox="0 0 8 8"><path d="M5.5 1L2.5 4l3 3" fill="none" stroke="#fff" stroke-width="1.6"/></svg></span>
  <div class="partner-list">
    <span>Synvetra</span>
    <span><i></i>Dalvoren</span>
    <span>Stonebay</span>
    <span>Kellmark Power</span>
    <span><i></i>Northfield Energy</span>
    <span>Telvane</span>
    <span>Harbor Suites</span>
  </div>
  <span class="round-arrow"><svg width="8" height="8" viewBox="0 0 8 8"><path d="M2.5 1l3 3-3 3" fill="none" stroke="#fff" stroke-width="1.6"/></svg></span>
</div>

<footer>
  <div class="footer-links abs">
    <span>Home</span><span>|</span><span>About Quorvanta</span><span>|</span><span>Benchmarking</span><span>|</span><span>Shop Quorvanta</span><span>|</span><span>News &amp; Events</span><span>|</span><span>Blog</span><span>|</span><span>Contact Us</span>
  </div>
  <div class="copyright abs"><span>Copyright ©&nbsp;&nbsp;2013</span><span>www.quorvanta.com</span><span>All rights reserved.</span></div>
  <div class="social abs" aria-label="Social links">
    <i style="background:#39a7e0"></i><i style="background:#1f6fa8"></i><i style="background:#333"></i>
  </div>
</footer>

</body>
</html>
```